Cedar Lantern Roots Gathering Music Conference & Concert Series needs a banner design to welco...

We are looking for a banner to use as a backdrop where people can take pictures and promote the event as they upload to social media. The music conference primarily targets high school students so we are looking for a design that will attract a younger audience. The festival revolves around music appreciation in the US/Mexico border. We like the "Cedar LanternRoots Gathering" trumpet logo on the "5th annual" design attached, but we are open to other designs.
Target Market(s)
ages 15-45
Colors
Designer to choose colors to be used in the design.
Look and feel

```html
<!DOCTYPE html>
<html lang="en">
<head>
<meta charset="utf-8">
<title>Cedar Lantern Roots Gathering – Music Conference &amp; Concert Series</title>
<link rel="stylesheet" href="https://fonts.googleapis.com/css2?family=Alfa+Slab+One&family=Oswald:wght@600&family=Questrial&display=swap">
<style>
  :root {
    --bg: #2e2e2e;
    --bg-glow: #383838;
    --ink: #ffffff;
    --rule: #1f93c9;
    --name-teal: #17e6c4;
    --name-yellow: #ffff1a;
    --name-green: #2ef03a;
    --art-light: #5a5a5a;
    --art-dark: #3a3a3a;
  }
  html, body {
    margin: 0;
    padding: 0;
    width: 1200px;
    height: 600px;
    overflow: hidden;
    background: var(--bg);
  }
  .banner {
    position: relative;
    width: 1200px;
    height: 600px;
    overflow: hidden;
    background: radial-gradient(ellipse at 60% 45%, var(--bg-glow) 0%, var(--bg) 70%);
  }
  .stage-art {
    position: absolute;
    left: 117px;
    top: 47px;
    width: 240px;
    height: 553px;
    border-radius: 110px 110px 0 0;
    background: linear-gradient(170deg, var(--art-light) 0%, var(--art-dark) 75%);
    opacity: 0.55;
  }
  .edition {
    position: absolute;
    left: 618px;
    top: 178px;
    margin: 0;
    font-family: "Oswald", sans-serif;
    font-weight: 600;
    font-size: 26px;
    letter-spacing: 1px;
    color: var(--ink);
    text-transform: uppercase;
    line-height: 1;
  }
  .rule {
    position: absolute;
    height: 7px;
    background: var(--rule);
  }
  .rule--top { left: 618px; top: 216px; width: 470px; }
  .rule--side { left: 465px; top: 337px; width: 95px; }
  .event-name {
    margin: 0;
    font-weight: 400;
    line-height: 1;
  }
  .event-name__line {
    position: absolute;
    white-space: nowrap;
  }
  .event-name__line--first {
    left: 465px;
    top: 236px;
    font-family: "Alfa Slab One", serif;
    font-size: 57px;
    font-variant: small-caps;
    letter-spacing: 0.5px;
  }
  .event-name__place { color: var(--name-teal); }
  .event-name__theme { color: var(--name-yellow); }
  .event-name__line--second {
    left: 647px;
    top: 326px;
    font-family: "Questrial", sans-serif;
    font-size: 56px;
    letter-spacing: 2px;
    color: var(--name-green);
  }
  .tagline {
    position: absolute;
    left: 654px;
    top: 400px;
    margin: 0;
    font-family: "Oswald", sans-serif;
    font-weight: 600;
    font-size: 23px;
    letter-spacing: 1.2px;
    color: var(--ink);
    text-transform: uppercase;
    line-height: 1;
  }
</style>
</head>
<body>
  <main class="banner">
    <div class="stage-art" role="img" aria-label="Line illustration of a hand holding a vintage stage microphone"></div>

    <p class="edition">5th Annual</p>
    <div class="rule rule--top"></div>
    <h1 class="event-name">
      <span class="event-name__line event-name__line--first"><span class="event-name__place">Cedar Lantern</span> <span class="event-name__theme">Roots</span></span>
      <span class="event-name__line event-name__line--second">Gathering</span>
    </h1>
    <div class="rule rule--side"></div>
    <p class="tagline">Music Conference &amp; Concert Series</p>
  </main>
</body>
</html>
```